Etiketten für Nahrungsergänzungsmittel
Zielgruppe
Wir stellen Nahrungsergänzungen her für psychische Gesundheit. Zielgruppe: jüngere Menschen 20-40 Jahre alt mit Interesse an Naturheilkunde. Firmenname: Velmora Works. Logo der Firma: s. Anhang
Aufgabenstellung
Dosenetikett 155 x 50 mm, für Kapseln mit Pflanzenextrakten aus Korallenbaum. Für besseren Schlaf und zur Beruhigung. Produktname: Sternkiesel

```html
<!DOCTYPE html>
<html lang="de">
<head>
<meta charset="utf-8">
<title>Sternkiesel – Dosenetikett</title>
<link rel="stylesheet" href="https://fonts.googleapis.com/css2?family=Fira+Sans:ital,wght@0,400;0,600;0,700;1,400;1,600&family=Patrick+Hand&display=swap">
<style>
  :root {
    --navy: #1b2a4a;
    --pink: #f7c1d3;
    --peach: #f2a07e;
    --ink: #15223f;
    --pale-blue: #9cb3cf;
    --white: #ffffff;
    --paper: #ffffff;
  }
  * { box-sizing: border-box; margin: 0; padding: 0; }
  html, body {
    width: 1200px; height: 2400px; overflow: hidden;
    background: var(--paper);
    font-family: "Fira Sans", Arial, sans-serif;
  }
  .label {
    position: absolute; left: 19px; top: 1339px;
    width: 1163px; height: 374px;
    background: var(--navy); overflow: hidden;
  }
  .pink-band { position: absolute; background: var(--pink); }
  .pink-band--top { left: 251px; top: 0; width: 912px; height: 203px; }
  .pink-band--left { left: 251px; top: 0; width: 327px; height: 296px; }

  .illustration {
    position: absolute; left: 284px; top: 100px; width: 434px; height: 274px;
    border-radius: 160px 160px 0 0;
    background: linear-gradient(120deg, var(--navy) 0%, var(--navy) 50%, var(--peach) 78%, #f5b08f 100%);
  }

  .info-panel {
    position: absolute; left: 0; top: 0; width: 251px; height: 374px;
    padding: 20px 22px 0 4px; text-align: right;
    color: var(--pale-blue); font-size: 11.8px; line-height: 14.5px;
    white-space: nowrap;
  }
  .info-panel h3 {
    font-style: italic; font-weight: 600; font-size: 11.8px; margin-top: 5px;
  }
  .info-panel h3:first-child { margin-top: 0; }
  .best-before { margin-top: 1px; }
  .field { display: inline-block; width: 54px; height: 12px; background: var(--white); vertical-align: middle; }
  .field--short { width: 43px; }
  .maker { margin-top: 26px; }
  .maker .web { font-style: italic; font-weight: 600; }

  .brand {
    position: absolute; left: 380px; top: 26px; width: 116px; text-align: center;
    color: var(--ink); font-weight: 700; font-size: 13.5px;
  }
  .brand-dot {
    display: block; width: 50px; height: 50px; border-radius: 50%;
    background: var(--ink); margin: 0 auto 8px;
  }

  .product-title {
    position: absolute; left: 518px; top: 10px;
    font-family: "Patrick Hand", "Comic Sans MS", cursive;
    font-size: 66px; line-height: 54px; color: var(--ink); letter-spacing: 1px;
    font-weight: 400;
  }
  .product-title span { display: block; }
  .product-title span:last-child { margin-left: -8px; }

  .claim {
    position: absolute; left: 592px; top: 136px;
    color: var(--ink); font-weight: 700; font-size: 13px; line-height: 15px;
  }
  .claim span { display: block; }
  .claim span:first-child { padding-left: 12px; }

  .extract {
    position: absolute; left: 637px; top: 218px;
    font-family: "Patrick Hand", "Comic Sans MS", cursive;
    color: var(--white); font-size: 25px; line-height: 23px;
  }
  .extract small { display: block; font-size: 13px; line-height: 11px; }

  .quantity {
    position: absolute; left: 335px; top: 340px;
    font-family: "Patrick Hand", "Comic Sans MS", cursive;
    color: var(--white); font-size: 19px;
  }

  .legal {
    position: absolute; left: 874px; top: 210px; width: 182px;
    color: var(--pale-blue); font-size: 12px; line-height: 13.5px;
  }
  .legal h3 { font-style: italic; font-weight: 600; font-size: 12px; }
  .legal .spaced { letter-spacing: 1.6px; margin-bottom: 6px; }
  .legal p { text-align: justify; }
  .legal .note { margin-top: 3px; text-align: left; }
</style>
</head>
<body>
  <section class="label">
    <div class="pink-band pink-band--top"></div>
    <div class="pink-band pink-band--left"></div>

    <div class="illustration" role="img" aria-label="Illustration: schlafendes Paar mit langem nachtblauem Haar voller Sterne und einer Mondsichel"></div>

    <aside class="info-panel">
      <h3>Zutatenliste:</h3>
      <p>Gemahlener Extrakt aus<br>Korallenbaumwurzel,<br>Cellulose-Kapsel</p>
      <h3>Empfohlene Tagesverzehrmenge:</h3>
      <p>pro 100G 100G Mulungu<br>pro 100G 10mg Erythravin</p>
      <h3>Verzehrempfehlung:</h3>
      <p>Ein- bis Zweimal täglich je eine Kapsel<br>zu den Mahlzeiten einnehmen.<br>Tägliche Verzehrmenge<br>nicht überschreiten.</p>
      <h3>mindestens haltbar</h3>
      <p class="best-before">bis Ende: <span class="field"></span> Lot-Nr. <span class="field field--short"></span></p>
      <p class="maker">Hergestellt in Deutschland<br>Velmora Works GmbH<br>Lindenhofer Str. 42B<br>D-58312 Hagen<br><span class="web">www.velmora-works.de</span></p>
    </aside>

    <div class="brand"><span class="brand-dot"></span>Velmora Works</div>

    <h1 class="product-title"><span>Stern-</span><span>kiesel</span></h1>

    <p class="claim"><span>Für besseren Schlaf</span><span>&amp; zur Beruhigung</span></p>

    <p class="extract">Extrakt<small>aus der</small>Korallen-<br>baumwurzel</p>

    <p class="quantity">90 Kapseln à 500 mg</p>

    <div class="legal">
      <h3>Zutaten:</h3>
      <p class="spaced">Mulunguextrakt</p>
      <h3>Nahrungsergänzungsmittel</h3>
      <p>sollte nicht als Ersatz für eine ausgewogene und abwechs­lungsreiche Ernährung verwen­det werden.</p>
      <p class="note">Außerhalb der Reichweite kleiner Kinder aufbewahren.</p>
      <p class="note">Kühl und trocken lagern.</p>
    </div>
  </section>
</body>
</html>
```